Packaging Design; Branding for Beer bottle label

I need to design a beer bottle label as a gift for my partners bday. It is part of a bigger present - a home brew beer kit, but the labels will be the icing on the cake.
I am very open to how it could look - but want it to be trendy and something he would be proud to present to friends (my partner is early 30's). I have had a caricature of his face drawn that i would like to use - it is attached in b&w but would be happy for someone to colour it? -either way, this should be incorporated in the design, somehow.
The beer brand is to be called 'Plimsoll Brewing Co' est 2018 and the label needs a small white space (cleverly incorporated) for him to hand write the brew - eg' Lager, Cider etc and a batch date. see attached 'label idea'.
Please minimize use of colour; green - any questions, just ask!

The beer will be bottled in Amber colour bottles.

His eye colour is blue

Target Market(s)

Men
Aged 30+

Colors

Designer to choose colors to be used in the design.

Requirements
Must have
• Caricature incorporated
• Name 'Plimsoll's Brewing Co'
• Est date 'est 2018'
• white space for beer type 'Brew', ABV% and brew date 'Batch' hand written on.
Nice to have
• Inspiration included as attachmentsq
Should not have
• Limited use of colour green

```html
<!DOCTYPE html>
<html lang="en">
<head>
<meta charset="utf-8">
<title>Plimsoll's Brewing Co – Bottle Label</title>
<link href="https://fonts.googleapis.com/css2?family=PT+Serif:wght@400;700&family=Montserrat:wght@500&display=swap" rel="stylesheet">
<style>
  :root {
    --page: #ffffff;
    --label: #e6e6e6;
    --green: #0b6b35;
    --ink: #111111;
    --art-light: #dfe9e1;
    --art-mid: #a9c8b2;
  }
  html, body {
    margin: 0;
    padding: 0;
    width: 1200px;
    height: 990px;
    overflow: hidden;
    background: var(--page);
  }
  .canvas {
    position: relative;
    width: 1200px;
    height: 990px;
  }
  .label {
    position: absolute;
    left: 111px;
    top: 230px;
    width: 976px;
    height: 551px;
    background: var(--label);
  }
  .band {
    position: absolute;
    left: 0;
    width: 100%;
    height: 9px;
    background: var(--green);
  }
  .band--top { top: 19px; }
  .band--bottom { top: 520px; }

  .brand__rule {
    position: absolute;
    left: 155px;
    top: 105px;
    width: 355px;
    height: 2px;
    background: var(--green);
  }
  .brand__name {
    position: absolute;
    left: 118px;
    top: 112px;
    width: 440px;
    margin: 0;
    text-align: center;
    font-family: "PT Serif", Georgia, serif;
    font-weight: 700;
    font-size: 82px;
    line-height: 1;
    color: var(--ink);
    transform: scaleX(0.74);
    transform-origin: center;
  }
  .brand__sub {
    position: absolute;
    left: 118px;
    top: 214px;
    width: 440px;
    margin: 0;
    text-align: center;
    font-family: "PT Serif", Georgia, serif;
    font-weight: 400;
    font-size: 28px;
    line-height: 1;
    letter-spacing: 4px;
    color: var(--ink);
  }
  .brand__est {
    position: absolute;
    left: 118px;
    top: 256px;
    width: 440px;
    margin: 0;
    text-align: center;
    font-family: "Montserrat", Arial, sans-serif;
    font-weight: 500;
    font-size: 13px;
    letter-spacing: 1px;
    color: var(--green);
  }

  .batch-form {
    position: absolute;
    left: 193px;
    top: 343px;
    width: 280px;
    margin: 0;
    padding: 0;
    list-style: none;
  }
  .batch-form__field {
    height: 44px;
    border-bottom: 2px dotted var(--green);
    box-sizing: border-box;
    font-family: "PT Serif", Georgia, serif;
    font-size: 29px;
    line-height: 40px;
    color: var(--green);
  }
  .batch-form__name {
    display: inline-block;
    transform: scaleX(0.88);
    transform-origin: left;
  }

  .caricature {
    position: absolute;
    left: 535px;
    top: 51px;
    width: 377px;
    height: 438px;
    border-radius: 46% 46% 30% 30%;
    background: radial-gradient(ellipse at 55% 40%, var(--art-light) 0%, var(--art-mid) 100%);
  }
</style>
</head>
<body>
  <div class="canvas">
    <section class="label">
      <div class="band band--top"></div>

      <header class="brand">
        <div class="brand__rule"></div>
        <h1 class="brand__name">PLIMSOLL'S</h1>
        <p class="brand__sub">BREWING CO</p>
        <p class="brand__est">EST. 2018</p>
      </header>

      <ul class="batch-form">
        <li class="batch-form__field"><span class="batch-form__name">BREW</span></li>
        <li class="batch-form__field"><span class="batch-form__name">ABV</span></li>
        <li class="batch-form__field"><span class="batch-form__name">DATE</span></li>
      </ul>

      <div class="caricature" role="img" aria-label="Green ink portrait illustration area"></div>

      <div class="band band--bottom"></div>
    </section>
  </div>
</body>
</html>
```